We are looking for a simple design that would be uplifting for
upscale drug addicts

MERIDIAN COLLECTIVE

PLEASE SEE THE LINK FOR TAG LINE AND CONTENT

thank you.

here is all the actual info we need and we want something like this...

http://files.qzr.lumtrabox.example/rest/objects/7c2910e4b557d81a93e40bd59fa644163fe2adf0899f?uid=bdf8e1b9b6f556b6b83c44471fdc79%2fproofs&expires=1482716603&signature=kT9PwLmQxZbVoNHLdtrtlmoGHQB%3d

The shape and colors don't have to be like what I posted it is only an example.

Target Market(s)

Harlow Row, internet and creative types, men, early 30's,
upwardly mobile, drug addicts

current site

brightkestrelway.example

now launching new name Meridian Collective

Industry/Entity Type

Drug

Requirements
Must have
• upscale look, great font
Should not have
• a corporate look but should not look like a clinic.

```html
<!DOCTYPE html>
<html lang="en">
<head>
<meta charset="utf-8">
<title>Meridian Collective – Business Card</title>
<link rel="stylesheet" href="https://fonts.googleapis.com/css2?family=Roboto+Condensed:wght@700&family=Roboto:wght@300&display=swap">
<style>
  :root {
    --backdrop: #e6e7e8;
    --card-black: #0c0c0c;
    --panel-grey: #3c3c3c;
    --ink-white: #ffffff;
  }
  * { margin: 0; padding: 0; box-sizing: border-box; }
  html, body {
    width: 1200px;
    height: 1000px;
    overflow: hidden;
    background: var(--backdrop);
  }
  .business-card {
    position: absolute;
    left: 100px;
    top: 182px;
    width: 994px;
    height: 611px;
    background: var(--card-black);
  }
  .info-panel {
    position: absolute;
    left: 94px;
    top: 135px;
    width: 900px;
    height: 340px;
    background: var(--panel-grey);
    border-radius: 8px 0 0 8px;
  }
  .wordmark {
    position: absolute;
    left: 22px;
    top: 49px;
    width: 834px;
    height: 110px;
    display: block;
  }
  .wordmark-rule { fill: var(--ink-white); }
  .wordmark-name {
    fill: var(--ink-white);
    font-family: "Roboto Condensed", "Arial Narrow", sans-serif;
    font-weight: 700;
    font-size: 90px;
  }
  .contact-block {
    position: absolute;
    top: 202px;
    font-family: "Roboto", "Helvetica Neue", Arial, sans-serif;
    font-weight: 300;
    font-size: 25px;
    line-height: 29px;
    color: var(--ink-white);
    white-space: nowrap;
  }
  .contact-block .line-gap { margin-top: 3px; }
  .contact-phones { left: 22px; }
  .contact-address { left: 554px; }
</style>
</head>
<body>
  <div class="business-card">
    <div class="info-panel">
      <svg class="wordmark" viewBox="0 0 834 110" aria-label="Meridian Collective">
        <rect class="wordmark-rule" x="0" y="0" width="834" height="3"/>
        <text class="wordmark-name" x="0" y="84" textLength="784" lengthAdjust="spacingAndGlyphs">MERIDIAN COLLECTIVE</text>
        <rect class="wordmark-rule" x="0" y="104" width="834" height="3"/>
      </svg>
      <div class="contact-block contact-phones">
        <p>Phone - (212) 555-0173</p>
        <p>Get Help Now - 24-Hour Hotline</p>
        <p class="line-gap">855-MER-RECOVER (855-555-0148)</p>
      </div>
      <address class="contact-block contact-address" style="font-style:normal">
        <p>418 West 52nd St.</p>
        <p>Suite 310</p>
        <p class="line-gap">New York, NY 10036</p>
      </address>
    </div>
  </div>
</body>
</html>
```